creating professional text layers for Bramwell Product listings images

I need some text added to several images in a professional eye catching way. The text should be legible on desktop and mobile devices. Rough mocks will be provided. You will just need to make them pop and professional. There are 10 images required in total to the selected designer. Below are just 3 of them

```html
<!DOCTYPE html>
<html lang="en">
<head>
<meta charset="utf-8">
<title>Bramwell listing banners</title>
<link href="https://fonts.googleapis.com/css2?family=Montserrat:wght@700;900&family=Saira+Condensed:wght@400;600;700&family=Kaushan+Script&display=swap" rel="stylesheet">
<style>
  :root{
    --stage:#4a4a4a;
    --stage-band:#3f3f3f;
    --gold:#f0a200;
    --gold-deep:#c98400;
    --ink:#0d0d0d;
    --white:#ffffff;
    --muted:#8c8a72;
  }
  html,body{margin:0;padding:0;overflow:hidden}
  body{width:1200px;height:851px;background:var(--stage);position:relative;font-family:"Saira Condensed",sans-serif}
  .row-divider{position:absolute;left:0;top:412px;width:1200px;height:14px;background:var(--stage-band)}
  .row-label{position:absolute;left:37px;transform:translate(-50%,-50%) rotate(-90deg);white-space:nowrap;color:var(--white);font-family:"Montserrat",sans-serif;font-weight:700;font-size:20px;letter-spacing:4px}
  .banner{position:absolute;width:358px;height:359px;overflow:hidden;box-sizing:border-box}
  .photo{position:absolute;inset:0}
  .text{position:absolute;color:var(--white);line-height:.92;text-transform:uppercase}

  /* new row frames */
  .frame-fade{padding:7px;background:linear-gradient(90deg,#141414 0%,#2a2100 35%,var(--gold) 70%,var(--gold) 100%)}
  .frame-full{padding:8px;background:var(--gold)}
  .frame-fade .inner,.frame-full .inner{position:relative;width:100%;height:100%;overflow:hidden}

  .new-head{right:18px;top:20px;text-align:right;font-weight:700}
  .new-head .l1{font-size:40px}
  .new-head .l2{font-size:54px;color:var(--gold)}
  .new-head .l3{font-size:33px}
  .new-head .l3.spaced{font-weight:400;letter-spacing:6px;font-size:34px}
  .question-box{position:absolute;right:12px;top:152px;width:136px;height:180px;border:1.5px solid var(--gold);border-right-width:1.5px}
  .question{position:absolute;right:22px;top:158px;text-align:right;font-size:25px;line-height:1.04;text-transform:none}
  .question.muted{color:var(--muted)}

  .pays-head{left:18px;top:24px;font-weight:700}
  .pays-head .l1{font-size:38px}
  .pays-head .l2{font-size:60px;margin-top:-2px}
  .pays-head .script{font-family:"Kaushan Script",cursive;text-transform:none;color:var(--gold);font-size:66px;transform:rotate(-6deg);transform-origin:left;margin-top:-14px;margin-left:4px}

  /* old row */
  .old{font-family:"Montserrat",sans-serif;font-weight:900;letter-spacing:-1.6px}
  .old-head{right:8px;top:16px;text-align:right;font-size:33px;line-height:.98}
  .old-question{right:8px;top:124px;text-align:right;font-size:26px;line-height:.96;color:var(--ink)}
  .old-pays{left:24px;top:18px;font-size:60px;line-height:.92;letter-spacing:-2.5px}
  .old-shadow{text-shadow:0 2px 4px rgba(0,0,0,.7)}
  .old-black-band{position:absolute;right:0;top:0;width:190px;height:118px;background:var(--ink)}
</style>
</head>
<body>
  <div class="row-divider"></div>
  <div class="row-label" style="top:222px">BRAMWELL NEW BANNER</div>
  <div class="row-label" style="top:640px">BRAMWELL OLD BANNER</div>

  <!-- new row -->
  <section class="banner frame-fade" style="left:72px;top:38px">
    <div class="inner">
      <div class="photo" role="img" aria-label="Wire stripping machine with speed dial and emergency stop, on a dark background" style="background:linear-gradient(100deg,#cfc8b4 0%,#8d8a80 30%,#2b2b2b 55%,#0b0b0b 75%)"></div>
      <div class="text new-head"><div class="l1">Variable</div><div class="l2">Speed</div><div class="l3">Control</div></div>
      <div class="question-box"></div>
      <div class="text question muted">How<br>Could You<br>Possibly<br>Strip All<br>Gauges At The<br>Same Speed?</div>
    </div>
  </section>

  <section class="banner frame-full" style="left:445px;top:38px">
    <div class="inner">
      <div class="photo" role="img" aria-label="Person standing behind a wire stripping machine on a wooden bench with copper wire" style="background:linear-gradient(180deg,#141414 0%,#242424 55%,#b79876 75%,#d8c2a2 100%)"></div>
      <div class="text pays-head"><div class="l1">Pays For</div><div class="l2">Itself</div><div class="script">Fast</div></div>
    </div>
  </section>

  <section class="banner frame-fade" style="left:811px;top:38px">
    <div class="inner">
      <div class="photo" role="img" aria-label="Close-up of the machine control box with speed dial and emergency stop in a workshop" style="background:linear-gradient(100deg,#8c8f92 0%,#d9d2b8 22%,#5a5c60 45%,#151515 62%,#0b0b0b 100%)"></div>
      <div class="text new-head"><div class="l1">Variable</div><div class="l2">Speed</div><div class="l3 spaced">Control</div></div>
      <div class="question-box"></div>
      <div class="text question">How<br>Could You<br>Possibly<br>Strip All<br>Gauges At The<br>Same Speed?</div>
    </div>
  </section>

  <!-- old row -->
  <section class="banner old" style="left:71px;top:461px">
    <div class="photo" role="img" aria-label="Wire stripping machine on a light wooden bench" style="background:linear-gradient(100deg,#cfc8b4 0%,#9a968b 35%,#d8b990 60%,#e2c9a4 100%)"></div>
    <div class="old-black-band"></div>
    <div class="text old-head">Variable<br>Speed<br>Control</div>
    <div class="text old-question">How<br>Could<br>You<br>Possibly<br>Strip All<br>Gauges<br>At The Same<br>Speed?</div>
  </section>

  <section class="banner old" style="left:441px;top:461px">
    <div class="photo" role="img" aria-label="Person standing behind a wire stripping machine on a wooden bench with copper wire" style="background:linear-gradient(180deg,#1c1e1f 0%,#2a2c2d 55%,#b79876 72%,#ddc8a8 100%)"></div>
    <div class="text old-pays old-shadow">Pays<br>For<br>Itself<br>Fast</div>
  </section>

  <section class="banner old" style="left:811px;top:461px">
    <div class="photo" role="img" aria-label="Close-up of the machine control box with speed dial and emergency stop in a workshop" style="background:linear-gradient(100deg,#6f7275 0%,#d9d2b8 25%,#6a6d70 50%,#9a9c9e 75%,#7a7c7e 100%)"></div>
    <div class="text old-head old-shadow" style="font-size:34px;top:26px">Variable<br>Speed<br>Control</div>
    <div class="text old-question old-shadow" style="color:var(--white);top:136px;font-size:24px">How<br>Could<br>You<br>Possibly<br>Strip All<br>Gauges<br>At The Same<br>Speed?</div>
  </section>
</body>
</html>
```